Seventh Ridge Wine Labels

Seventh Ridge is an ultra-premium, allocation-only Napa Valley wine brand being built with one objective: to become a long-term cult collectible.

This is not a retail wine.
This is not a lifestyle brand.
This is not driven by marketing trends.

Production is intentionally limited. Access is controlled through private membership. Every decision—from vineyard sourcing to packaging—is made with long-term brand equity in mind.
We are looking for a label system that reflects that level of discipline.

Design a cult-level wine label system for Seventh Ridge that communicates rarity, restraint, and authority at a glance.

This is not decorative Napa.
This must feel like it belongs next to Lanternfield, Corvath, Bellwether—and still stand apart.
Brand Positioning
Ultra-premium, allocation-only Napa wine
Private membership model (not retail-driven)
Production capped intentionally (scarcity is real, not marketing)
Designed to become a long-term collectible

Tone:

Controlled
Intentional
Confident
Understated power

If it feels “designed” or “trying”—it’s wrong.

Core Product Structure

You are designing a system, not a single label.

Foundation Wines:

Cabernet Sauvignon (primary SKU)
Signature Blend

Extensions (future / limited):

Limited Edition Blend (art-driven)
Reserve (ultra minimal, elevated version)
Creative Direction (Critical)

We are pursuing cult minimalism with tension.

Think:

Silence > noise
Precision > decoration
Material > graphics

This should feel:

Like it was inevitable, not created
Recognizable from across the room
Memorable after one exposure
Design Constraints

These are non-negotiable:

Bottle: Velmont Astrano (tall, powerful silhouette)
Glass: Deep antique green (near black)
Capsule: Matte black (baseline)
Front must work with:
Direct glass etching (ghost etch) OR
Minimal premium paper label

No loud colors.
No trendy typography.
No illustrative storytelling.

Brand Elements to Use
Primary mark: VII (Roman numeral 9)
Brand name: SEVENTH RIDGE
Vintage (subtle, not dominant)

Optional concept element:

Varietal composition expressed as a refined system (e.g., “85 · 15” or structured numeric expression)
Design Goals

Your design should achieve:

Instant Recognition
Must be identifiable from 10 feet away
Tactile Value
Feels expensive before you touch it
Even better once you do
Aging Power
This must still look relevant in 20 years
System Cohesion
Cabernet and Blend must feel like a family
Not two separate brands
What We Are NOT Looking For

Avoid immediately:

Gold foil overload
Script fonts / calligraphy
Illustrated vineyards / animals / crests
Trendy “modern winery” aesthetics
Busy compositions
Obvious luxury clichés

If it looks like:

A Napa tasting room brand → reject
A startup wine brand → reject
Something you'd see on a grocery shelf → reject
Creative Territories to Explore

Designers should explore distinct directions, not minor variations:

Pure Etch Minimalism
VII only
Extremely subtle, almost invisible
Power through absence
Architectural Typography
Strong, controlled use of SEVENTH RIDGE
Spatial tension, alignment-driven
Symbol + System
VII + numeric composition (85 / 15, etc.)
Feels like a formula, not decoration
Material-Driven Label
Paper, emboss, deboss, letterpress
Texture carries the design

Target Market(s)

Ultra-high-net-worth individuals, collectors, and allocation-driven wine buyers. Men and women 35–65 Entrepreneurs, executives, investors Already purchasing cult Napa wines ($250–$1,000+ per bottle) Psychographics: Value scarcity over availability Prefer private access over retail Buy for status, cellar, and long-term collection Appreciate restraint, not flash If it appeals to mass retail, it’s wrong.

Industry/Entity Type

Luxury Wine / Fine Wine / Ultra-Premium Consumer Goods

Requirements
Must have
• 1. Lanternfield Why it matters: True cult positioning Feels rare, quiet, and collector-driven What to take: Effortless authority Doesn’t try to look expensive—it just is Strong identity without noise What to avoid: Do not replicate illustration or vintage storytelling style 2. Bellwether (Corvath Family) Why it matters: Masterclass in restraint and architectural design What to take: Minimalism with structure Precision typography and spacing Confidence through reduction What to avoid: Don’t make it cold or overly corporate 3. Corvath Estate Why it matters: One of the most iconic luxury wine labels ever What to take: Timelessness Balance of tradition + authority Label presence without excess What to avoid: Avoid classic/heritage clichés (crests, shields, etc.) 4. Tarsel Nine Why it matters: Instantly recognizable globally Clean, iconic silhouette and branding system What to take: Immediate recognition from distance Cohesive system across vintages What to avoid: Don’t go mainstream or overly commercial 5. Silent Heron Why it matters: Pure scarcity-driven brand power What to take: Understated exclusivity Nothing feels added for effect What to avoid: Do not introduce illustration or narrative-driven visuals

```html
<!DOCTYPE html>
<html lang="en">
<head>
<meta charset="utf-8">
<title>Seventh Ridge — Cabernet Sauvignon Label</title>
<link rel="stylesheet" href="https://fonts.googleapis.com/css2?family=Cormorant+Garamond:ital,wght@0,400;0,500;1,400;1,500&display=swap">
<style>
  :root {
    --backdrop: #f2f2f0;
    --paper: #f7f7f5;
    --paper-shade: #ececea;
    --ink-grey: #8a8a88;
    --wine-red: #b3403f;
    --gold: #b8872f;
    --slate: #2c2e33;
    --slate-deep: #1f2125;
  }
  * { margin: 0; padding: 0; box-sizing: border-box; }
  html, body {
    width: 1200px;
    height: 1200px;
    overflow: hidden;
    background: var(--backdrop);
  }
  .label {
    position: absolute;
    left: 250px;
    top: 100px;
    width: 700px;
    height: 1000px;
    background: linear-gradient(180deg, var(--paper) 0%, var(--paper-shade) 100%);
    font-family: "Cormorant Garamond", Georgia, serif;
    overflow: hidden;
    box-shadow: 0 2px 14px rgba(0,0,0,0.08);
  }
  .brand-name {
    position: absolute;
    top: 218px;
    left: 0;
    width: 100%;
    text-align: center;
    font-size: 38px;
    font-weight: 400;
    letter-spacing: 0.12em;
    color: var(--ink-grey);
  }
  .varietal {
    position: absolute;
    top: 344px;
    width: 100%;
    text-align: center;
    font-style: italic;
    font-size: 32px;
    letter-spacing: 0.06em;
    color: var(--wine-red);
  }
  .vintage {
    position: absolute;
    top: 382px;
    width: 100%;
    text-align: center;
    font-size: 22px;
    letter-spacing: 0.14em;
    color: var(--ink-grey);
  }
  .terrain-band {
    position: absolute;
    left: 0;
    top: 515px;
    width: 100%;
    height: 485px;
  }
  .terrain-band svg { display: block; width: 100%; height: 100%; }
  .estate-mark {
    position: absolute;
    top: 838px;
    left: 250px;
    font-style: italic;
    font-weight: 500;
    font-size: 30px;
    color: var(--gold);
  }
</style>
</head>
<body>
  <main class="label">
    <div class="brand-name">SEVENTH RIDGE</div>
    <div class="varietal">Cabernet Sauvignon</div>
    <div class="vintage">v.2026</div>

    <div class="terrain-band" role="img" aria-label="Dark slate band with a faint topographic contour map of the vineyard">
      <svg viewBox="0 0 700 485" preserveAspectRatio="none">
        <defs>
          <linearGradient id="slate-fill" x1="0" y1="0" x2="1" y2="1">
            <stop offset="0" stop-color="#34363b"/>
            <stop offset="0.55" stop-color="#2a2c31"/>
            <stop offset="1" stop-color="#1f2125"/>
          </linearGradient>
        </defs>
        <path fill="url(#slate-fill)" d="M0 8 L20 5 L38 9 L60 4 L82 8 L104 3 L130 9 L152 5 L176 10 L200 4 L226 8 L250 3 L274 9 L300 5 L326 10 L350 4 L376 8 L400 3 L424 9 L450 5 L474 10 L500 4 L526 8 L550 3 L574 9 L600 5 L626 10 L650 4 L676 8 L700 5 L700 485 L0 485 Z"/>
      </svg>
    </div>

    <div class="estate-mark">7th Ridge</div>
  </main>
</body>
</html>
```